Label Design For My Pet Supplements Brand - Probiotic Dog Chews

Good Afternoon!
I am looking for a revamp of our current label design for my Probiotic Dog Chews. Attached is our current label and a mockup as well. I do like and appreciate our current design, but it lacks character, and appears to be really similar to other brands out there. I would like for the new label to take all the great characteristics of this label, but elevate them.
For context, our product is a 10oz White Jar with a White Lid.
I am attaching a full comprehensive guide that includes our existing files, fonts, .ai files, mockups, and our Brand Strategy. That way you're able to get an idea of what it is we sell and who exactly our customer is too. And that way we are able to create a label that speaks to our exact ideal customer. I am also supplying to you all the details for the label as well.
If you have any questions for me, feel free to ask. I'm looking forward to seeing your work!

```html
<!DOCTYPE html>
<html lang="en">
<head>
<meta charset="utf-8">
<title>Tailbloom Probiotic Chews – Label Colourways</title>
<link href="https://fonts.googleapis.com/css2?family=Anton&family=Montserrat:wght@500;800&display=swap" rel="stylesheet">
<style>
  :root {
    --bg: #ffffff;
    --teal: #76cbbd;
    --teal-deep: #5fbcac;
    --blue: #43b4f0;
    --blue-deep: #1f8fdc;
    --orange: #f3a06b;
    --orange-deep: #d25c18;
    --cream: #f6f0e6;
    --dog-brown: #6b3a22;
    --dog-white: #ece6dc;
    --chew-light: #f7b23a;
    --chew-deep: #ea6a1c;
  }
  * { margin: 0; padding: 0; box-sizing: border-box; }
  html, body { width: 1200px; height: 818px; overflow: hidden; background: var(--bg); }
  .canvas {
    position: relative; width: 1200px; height: 818px;
    display: flex; justify-content: center; align-items: center; gap: 40px;
  }
  .label {
    position: relative; width: 540px; height: 444px; overflow: hidden;
    font-family: "Anton", "Impact", sans-serif; color: var(--cream);
  }
  .label--teal { --accent: var(--teal); --accent-deep: var(--teal-deep); }
  .label--blue { --accent: var(--blue); --accent-deep: var(--blue-deep); }
  .hero-field {
    position: absolute; inset: 0 0 125px 0;
    background: linear-gradient(90deg, var(--accent-deep) 0%, var(--accent) 55%);
  }
  .flavor-band {
    position: absolute; left: 0; right: 0; bottom: 0; height: 125px;
    background: linear-gradient(90deg, var(--orange-deep) 0%, var(--orange) 45%);
  }
  .dog-photo {
    position: absolute; left: 45px; top: 18px; width: 211px; height: 301px;
    border-radius: 80px 90px 0 0;
    background: radial-gradient(ellipse at 55% 60%, var(--dog-white) 0%, #b7875d 35%, var(--dog-brown) 70%);
  }
  .brand-name {
    position: absolute; left: 281px; top: 28px; width: 210px; text-align: center;
    font-size: 46px; line-height: 1.1; letter-spacing: 1px; white-space: nowrap;
    text-transform: uppercase;
  }
  .product-title {
    position: absolute; left: 236px; top: 140px; width: 280px; text-align: center;
    font-weight: 400; line-height: 1; text-transform: uppercase; white-space: nowrap;
    transform: rotate(-4deg);
    text-shadow: 3px 4px 0 rgba(0,0,0,0.12);
  }
  .product-title .line-1 { display: block; font-size: 60px; letter-spacing: 1px; }
  .product-title .line-2 { display: block; font-size: 62px; letter-spacing: 2px; }
  .flavor {
    position: absolute; left: 128px; top: 340px; width: 120px; text-align: center;
    font-size: 19px; line-height: 1.1; letter-spacing: 0.5px; white-space: nowrap;
    text-transform: uppercase;
  }
  .flavor-arrow { position: absolute; left: 240px; top: 362px; }
  .chews-illustration {
    position: absolute; left: 298px; top: 308px; width: 100px; height: 84px;
    border-radius: 10px;
    background: linear-gradient(135deg, var(--chew-light), var(--chew-deep));
  }
  .facts-row {
    position: absolute; left: 0; right: 0; top: 409px; height: 26px;
    display: flex; align-items: center; justify-content: center; gap: 18px;
    font-family: "Montserrat", Arial, sans-serif; font-weight: 500; font-size: 11px;
    letter-spacing: 0.3px; white-space: nowrap;
  }
  .count-pill {
    background: var(--accent); border-radius: 13px; padding: 5px 18px;
    font-weight: 800; font-size: 15px; letter-spacing: 1px;
  }
</style>
</head>
<body>
<main class="canvas">
  <section class="label label--teal">
    <div class="hero-field"></div>
    <div class="flavor-band"></div>
    <div class="dog-photo" role="img" aria-label="Photo of a brown and white shepherd dog looking up"></div>
    <div class="brand-name">Tailbloom</div>
    <h1 class="product-title"><span class="line-1">Probiotic</span><span class="line-2">Chews</span></h1>
    <p class="flavor">Peanut Butter<br>Flavor</p>
    <svg class="flavor-arrow" width="56" height="30" viewBox="0 0 62 30" aria-hidden="true">
      <path d="M4 8 Q26 34 56 10" fill="none" stroke="#f6f0e6" stroke-width="2.5" stroke-linecap="round"/>
      <path d="M47 8 L57 9 L54 19" fill="none" stroke="#f6f0e6" stroke-width="2.5" stroke-linecap="round" stroke-linejoin="round"/>
    </svg>
    <div class="chews-illustration" role="img" aria-label="Illustration of three peanut butter chew cubes"></div>
    <div class="facts-row">
      <span>SUPPLEMENT FOR DOGS</span>
      <span class="count-pill">140 CT.</span>
      <span>NET CONTENTS 10 OZ.</span>
    </div>
  </section>

  <section class="label label--blue">
    <div class="hero-field"></div>
    <div class="flavor-band"></div>
    <div class="dog-photo" role="img" aria-label="Photo of a brown and white shepherd dog looking up"></div>
    <div class="brand-name">Tailbloom</div>
    <h1 class="product-title"><span class="line-1">Probiotic</span><span class="line-2">Chews</span></h1>
    <p class="flavor">Peanut Butter<br>Flavor</p>
    <svg class="flavor-arrow" width="56" height="30" viewBox="0 0 62 30" aria-hidden="true">
      <path d="M4 8 Q26 34 56 10" fill="none" stroke="#f6f0e6" stroke-width="2.5" stroke-linecap="round"/>
      <path d="M47 8 L57 9 L54 19" fill="none" stroke="#f6f0e6" stroke-width="2.5" stroke-linecap="round" stroke-linejoin="round"/>
    </svg>
    <div class="chews-illustration" role="img" aria-label="Illustration of three peanut butter chew cubes"></div>
    <div class="facts-row">
      <span>SUPPLEMENT FOR DOGS</span>
      <span class="count-pill">140 CT.</span>
      <span>NET CONTENTS 10 OZ.</span>
    </div>
  </section>
</main>
</body>
</html>
```